CBD PATCHES

Design creation of my CBD patch box.
Product must look Pharamaceutical grade.
Colours need to look pharmaceutical (green/white/maybe a bit of blue).
Text: Cannabidiol (CBD) Self-curing adhesive Polyethylene backing sheet.
Apply one patch to a smooth are of skin. Each patch can be worn for up to 24 hours. Apply subsequent patches to different areas to allow the skin to breathe between uses.
Do not apply to broken or irritable skin. Consult a doctor if you are taking medications or have medical conditions before using this or any other supplement. Do not use if you are pregnant or breastfeeding.
Store in a cool, dry place out of direct sunlight. Stable for three years. Once opened, use within 12 months.

```html
<!DOCTYPE html>
<html lang="en">
<head>
<meta charset="utf-8">
<title>CBD Patch Box – Dieline</title>
<link href="https://fonts.googleapis.com/css2?family=Archivo:wght@800&family=Roboto:wght@400;500&display=swap" rel="stylesheet">
<style>
  :root {
    --leaf-green: #bcdd47;
    --leaf-deep: #a9cc3a;
    --paper: #ffffff;
    --cut-line: #1a1a1a;
    --ink: #111111;
    --page: #ffffff;
  }
  html, body {
    margin: 0;
    padding: 0;
    width: 1200px;
    height: 1000px;
    overflow: hidden;
    background: var(--page);
  }
  .canvas {
    position: relative;
    width: 1200px;
    height: 1000px;
  }
  .dielines {
    position: absolute;
    inset: 0;
  }
  .instructions {
    position: absolute;
    left: 240px;
    width: 214px;
    font-family: "Roboto", Arial, sans-serif;
    font-size: 10.4px;
    line-height: 11.6px;
    color: var(--ink);
    text-align: justify;
  }
  .instructions p { margin: 0 0 11.6px; }
  .instructions--usage { top: 283px; }
  .instructions--storage { top: 447px; }

  .upside-down {
    position: absolute;
    transform: rotate(180deg);
  }
  .front-label {
    left: 740px;
    top: 305px;
    width: 235px;
    height: 195px;
  }
  .bottom-label {
    left: 732px;
    top: 518px;
    width: 246px;
    height: 125px;
  }
  .product-title {
    position: absolute;
    left: 30px;
    margin: 0;
    font-family: "Archivo", Arial, sans-serif;
    font-weight: 800;
    font-size: 24px;
    line-height: 26px;
    color: var(--leaf-green);
    letter-spacing: 0.3px;
  }
  .spec {
    position: absolute;
    left: 30px;
    margin: 0;
    font-family: "Roboto", Arial, sans-serif;
    font-size: 8.6px;
    line-height: 11px;
    color: var(--ink);
  }
  .brand-mark {
    position: absolute;
    left: 30px;
    top: 10px;
    display: flex;
    align-items: center;
    gap: 5px;
  }
  .brand-mark__dot {
    width: 30px;
    height: 30px;
    border-radius: 50%;
    background: var(--leaf-green);
  }
  .brand-mark__name {
    font-family: "Roboto", Arial, sans-serif;
    font-weight: 500;
    font-size: 7px;
    letter-spacing: 0.5px;
    color: var(--leaf-green);
  }
  .hemp-leaf {
    position: absolute;
    left: 140px;
    top: 92px;
    width: 85px;
    height: 96px;
    border-radius: 45% 45% 50% 50%;
    background: radial-gradient(circle at 50% 55%, var(--leaf-deep), #d2e87f 70%, rgba(210,232,127,0) 72%);
  }
</style>
</head>
<body>
<div class="canvas">
  <svg class="dielines" width="1200" height="1000" viewBox="0 0 1200 1000" xmlns="http://www.w3.org/2000/svg">
    <defs>
      <path id="box-outline" d="M208,145 H290 C292,125 318,112 350,112 C382,112 408,125 410,145 H483 V512 H520 C552,512 574,545 574,600 V768 H470 C462,768 455,774 455,782 V885 H380 C380,850 365,835 350,835 C335,835 320,850 320,885 H240 V782 C240,774 233,768 225,768 H118 V600 C118,545 140,512 172,512 H208 Z"/>
      <g id="fold-lines">
        <path d="M222,160 H300 C303,140 325,127 350,127 C375,127 397,140 400,160 H469 V262 H222 Z"/>
        <path d="M222,518 H469 V762 H222 Z"/>
        <path d="M222,643 H469"/>
        <path d="M222,528 H205 C165,528 132,560 132,610 V752 H222"/>
        <path d="M469,528 H486 C526,528 559,560 559,610 V752 H469"/>
        <path d="M160,648 L203,690"/>
        <path d="M527,648 L485,690"/>
        <path d="M295,660 L302,667 H388 L395,660"/>
        <path d="M255,772 V873 H330 C330,858 338,848 350,848 C362,848 370,858 370,873 H440 V772"/>
      </g>
    </defs>

    <!-- back dieline -->
    <use href="#box-outline" fill="var(--leaf-green)"/>
    <rect class="panel-white" x="208" y="265" width="275" height="173" fill="var(--paper)"/>

    <!-- front dieline -->
    <g transform="translate(510,0)">
      <use href="#box-outline" fill="var(--leaf-green)"/>
    </g>
    <rect class="panel-white" x="718" y="265" width="275" height="253" fill="var(--paper)"/>
    <path class="panel-swoosh" d="M718,263 H993 V288 C880,292 785,305 732,330 H718 Z" fill="var(--leaf-green)"/>
    <rect class="panel-white" x="732" y="518" width="246" height="125" fill="var(--paper)"/>
    <path class="panel-swoosh" d="M732,643 C780,616 880,603 978,600 V643 Z" fill="var(--leaf-green)"/>

    <!-- cut and fold lines -->
    <g fill="none" stroke="var(--cut-line)" stroke-width="1">
      <use href="#box-outline"/>
      <use href="#fold-lines"/>
      <g transform="translate(510,0)">
        <use href="#box-outline"/>
        <use href="#fold-lines"/>
      </g>
      <path d="M732,262 H978 M732,262 V518 M978,262 V518" stroke-width="0.5"/>
    </g>
  </svg>

  <div class="instructions instructions--usage">
    <p>Apply one patch to a smooth are of skin. Each patch can be worn for up to 24 hours. Apply subsequent patches to different areas to allow the skin to breathe between uses.</p>
    <p>Do not apply to broken or irritable skin. Consult a doctor if you are taking medications or have medical conditions before using this or any other supplement. Do not use if you are pregnant or breastfeeding.</p>
  </div>
  <div class="instructions instructions--storage">
    <p>Store in a cool, dry place out of direct sunlight. Stable for three years. Once opened, use within 12 months.</p>
  </div>

  <div class="upside-down front-label">
    <div class="brand-mark">
      <span class="brand-mark__dot"></span>
      <span class="brand-mark__name">VERDALIS</span>
    </div>
    <h1 class="product-title" style="top:72px;">Cannabidiol</h1>
    <p class="product-title" style="top:100px;">(CBD)</p>
    <p class="spec" style="top:140px;">Self-curing adhesive</p>
    <p class="spec" style="top:152px;">Polyethylene backing sheet</p>
    <div class="hemp-leaf" role="img" aria-label="Green hemp leaf illustration"></div>
  </div>

  <div class="upside-down bottom-label">
    <p class="product-title" style="top:52px;">Cannabidiol</p>
    <p class="product-title" style="top:80px;">(CBD)</p>
  </div>
</div>
</body>
</html>
```